Single page 8 1/2 x 11 flyer to entice new homeowners to visit our WEBSITE

A single page flyer that we can put on an easel that promotes our website, tallowpine58.com, to new homeowners for blinds, shades, bath hardware, cabinet organization, etc. This piece will be on an easel in sales centers, design studios and closing offices. We want the homeowners to know where they can go to get reliable products and service from a trusted partner of their builder for products that were not installed in their new home before they closed.

Enter the coupon code KQT10 to get 10% off of your entire purchase and free shipping. The product on our website will put the finishing touches on their home. ....make your house your home

Target Market(s)

New homebuyers

Industry/Entity Type

Residential Construction

Font styles to use
Serif

Colors
ec1f27

Requirements
Must have
• Logo and website, tallowpine58.com and tagline, make your house your home
Nice to have
• what will drive new homeowners to the website to purchase items they did not purchase before closing like window blinds and shades, bath hardware, ceiling fans, grills, electric fireplaces, etc.

```html
<!DOCTYPE html>
<html lang="en">
<head>
<meta charset="utf-8">
<title>Tallow Pine 58 – New Homeowner Flyer</title>
<link href="https://fonts.googleapis.com/css2?family=Roboto+Condensed:wght@400;700&family=Roboto:wght@400;700&display=swap" rel="stylesheet">
<style>
:root{
  --red:#d42027;
  --red-bright:#ec1f27;
  --ink:#161616;
  --grey:#a8a8a8;
  --badge-ring:#b8b8b8;
  --label-bg:rgba(60,60,60,.82);
  --paper:#ffffff;
  --stage:#e9e6e2;
}
*{margin:0;padding:0;box-sizing:border-box}
html,body{width:1200px;height:1200px;overflow:hidden;background:var(--stage)}
body{position:relative;font-family:"Roboto",sans-serif;color:var(--ink)}
.flyer{position:absolute;left:182px;top:59px;width:836px;height:1082px;background:var(--paper);overflow:hidden;box-shadow:0 6px 24px rgba(0,0,0,.18)}
.abs{position:absolute}
.cond{font-family:"Roboto Condensed",sans-serif}

.url-banner{left:22px;top:26px;width:792px;height:80px;background:var(--red);color:#fff;font-weight:700;font-size:50px;text-align:center;line-height:80px;letter-spacing:.5px;box-shadow:0 8px 10px -6px rgba(0,0,0,.45);z-index:3}
.url-pointer{left:220px;top:104px;width:0;height:0;border-left:10px solid transparent;border-right:10px solid transparent;border-top:10px solid var(--red);z-index:3}

.band{left:0;top:480px;width:836px;height:180px}

.photo{left:0;top:190px;width:440px;height:434px;
  background:linear-gradient(170deg,#d9d6e6 0%,#9096ad 30%,#6b7a99 55%,#7d8a6a 80%,#9aa58c 100%);
  -webkit-mask-image:linear-gradient(to right,#000 0%,#000 62%,transparent 100%),linear-gradient(to bottom,transparent 0%,#000 22%,#000 100%);
  -webkit-mask-composite:source-in;
  mask-image:linear-gradient(to right,#000 0%,#000 62%,transparent 100%),linear-gradient(to bottom,transparent 0%,#000 22%,#000 100%);
  mask-composite:intersect}

.tagline{left:60px;top:132px;width:320px;text-align:center;font-size:16px;z-index:2}
.steps{left:60px;top:156px;width:320px;text-align:center;font-size:24px;font-weight:700;word-spacing:14px;z-index:2}

.brand{left:436px;top:168px;width:390px;height:100px;display:flex;align-items:center;gap:16px}
.brand-dot{width:64px;height:64px;border-radius:50%;background:var(--red);flex:none}
.brand-name{font-family:"Roboto Condensed",sans-serif;font-weight:700;font-size:44px;line-height:1;color:var(--ink);white-space:nowrap}

.lead{left:400px;top:306px;width:420px;text-align:center;font-size:22px;font-weight:700;line-height:30px}
.headline{left:400px;top:370px;width:420px;text-align:center;font-size:40px;font-weight:700;line-height:50px}
.headline .red{color:var(--red-bright)}

.badge{border-radius:50%;background:var(--red);border:8px solid var(--badge-ring);display:flex;flex-direction:column;align-items:center;justify-content:center;color:#fff;z-index:2}
.badge-ship{left:68px;top:492px;width:192px;height:192px}
.ship-art{width:130px;height:112px;border-radius:6px;background:linear-gradient(135deg,#d8b27a,#a97c44)}

.minimums{left:286px;top:548px;font-size:24px;color:#fff;line-height:32px}

.badge-off{left:444px;top:492px;width:192px;height:192px}
.off-text{transform:rotate(-7deg);text-align:center;font-family:"Roboto Condensed",sans-serif;font-weight:700}
.off-big{font-size:68px;line-height:60px;letter-spacing:-3px}
.off-big small{font-size:26px;letter-spacing:0}
.off-sub{font-size:23px;line-height:25px}

.benefits{left:654px;top:532px;font-size:21px;font-weight:700;line-height:25px;color:#fff}
.promo{left:636px;top:628px;font-size:16px;color:var(--ink)}

.tile{overflow:hidden}
.tile .label{position:absolute;left:0;right:0;bottom:0;height:34px;line-height:34px;background:var(--label-bg);color:#fff;text-align:center;font-family:"Roboto Condensed",sans-serif;font-weight:700;font-size:17px;letter-spacing:.3px}
.tile .art{position:absolute;inset:0}

.t1{left:0;top:656px;width:160px;height:124px}
.t2{left:160px;top:656px;width:160px;height:124px}
.t3{left:320px;top:656px;width:164px;height:124px}
.t4{left:484px;top:656px;width:184px;height:124px}
.t5{left:668px;top:656px;width:168px;height:124px}
.t6{left:0;top:780px;width:192px;height:128px}
.t7{left:192px;top:780px;width:214px;height:128px}
.t8{left:406px;top:780px;width:254px;height:128px}
.t9{left:660px;top:780px;width:176px;height:128px}

.closing{left:0;top:918px;width:836px;text-align:center}
.closing .c1{color:var(--red-bright);font-size:19px}
.closing .c2{font-size:18px;font-weight:700;margin-top:2px}
.closing .c3{font-size:15px;margin-top:2px}

.rule{left:0;top:1004px;width:836px;height:10px;background:#bdbdbd}
.footer{left:0;top:1016px;width:836px;height:66px;background:var(--red);color:#fff;font-family:"Roboto Condensed",sans-serif;font-size:26px;line-height:66px;text-align:center;word-spacing:2px}
.footer span+span{margin-left:24px}
</style>
</head>
<body>
<main class="flyer">

  <div class="abs url-banner">www.tallowpine58.com</div>
  <div class="abs url-pointer"></div>

  <svg class="abs band" viewBox="0 0 836 180" preserveAspectRatio="none" aria-hidden="true">
    <path d="M0 60 Q300 -10 836 26 L836 142 L0 142 Z" fill="#1e1e1e"/>
    <path d="M0 70 Q330 8 836 40 L836 142 L0 142 Z" fill="var(--red)"/>
    <rect x="0" y="142" width="836" height="34" fill="var(--grey)"/>
  </svg>

  <div class="abs photo" role="img" aria-label="Photo of an older couple from behind, arm in arm, looking at their new two-storey house at dusk"></div>

  <p class="abs tagline">Your Home | Your Project | Your Way</p>
  <p class="abs steps cond">Measure Order Install</p>

  <div class="abs brand">
    <span class="brand-dot"></span>
    <span class="brand-name">TALLOW PINE 58</span>
  </div>

  <p class="abs lead cond">The product on our website will<br>put the finishing touches on your home.....</p>
  <h1 class="abs headline cond"><span class="red">MAKE YOUR HOUSE</span><br>YOUR HOME</h1>

  <div class="abs badge badge-ship">
    <div class="ship-art" role="img" aria-label="Cardboard shipping box wrapped with a red arrow reading free shipping"></div>
  </div>

  <p class="abs minimums">No<br>Minimums</p>

  <div class="abs badge badge-off">
    <div class="off-text">
      <div class="off-big">10<small>%OFF</small></div>
      <div class="off-sub">YOUR ENTIRE<br>PURCHASE</div>
    </div>
  </div>

  <p class="abs benefits cond">COMFORT<br>FUNCTIONALITY<br>UPGRADE</p>
  <p class="abs promo">Use Promo Code&nbsp; KQT10</p>

  <div class="abs tile t1"><div class="art" role="img" aria-label="Pull-out cabinet organizer with bin" style="background:linear-gradient(90deg,#3b3b3b,#8a8a8a 40%,#e8e8e8 60%,#9a7a5a)"></div><div class="label">CABINET</div></div>
  <div class="abs tile t2"><div class="art" role="img" aria-label="Brushed nickel ceiling fan with wood blades" style="background:linear-gradient(180deg,#fff,#f1ece8 60%,#fff)"></div><div class="label">CEILING FANS</div></div>
  <div class="abs tile t3"><div class="art" role="img" aria-label="Wood cabinet doors with metal pulls" style="background:linear-gradient(90deg,#7a4b2c,#a96f45 50%,#6b3f24)"></div><div class="label">CABINET HARDWARE</div></div>
  <div class="abs tile t4"><div class="art" role="img" aria-label="Wood blinds over a window" style="background:linear-gradient(180deg,#9a5a44,#c0917a)"></div><div class="label">WOOD BLINDS</div></div>
  <div class="abs tile t5"><div class="art" role="img" aria-label="Stainless steel gas grill" style="background:linear-gradient(180deg,#f4f4f4,#b9bcbf 50%,#6d7176)"></div><div class="label">GRILLS</div></div>
  <div class="abs tile t6"><div class="art" role="img" aria-label="Kitchen with pendant lighting" style="background:linear-gradient(180deg,#f1efe9,#c9c3b6 55%,#5b4a3a)"></div><div class="label">LIGHTING</div></div>
  <div class="abs tile t7"><div class="art" role="img" aria-label="Chrome toilet paper holder" style="background:linear-gradient(180deg,#fff,#f0f0f0)"></div><div class="label">BATH HARDWARE</div></div>
  <div class="abs tile t8"><div class="art" role="img" aria-label="Wall-mounted electric fireplace with flames" style="background:linear-gradient(180deg,#2a2a2a,#1a1a1a 45%,#c8582a 58%,#2a2a2a 70%,#444)"></div><div class="label">ELECTRIC FIREPLACES</div></div>
  <div class="abs tile t9"><div class="art" role="img" aria-label="Grey roller shades on bright windows" style="background:linear-gradient(180deg,#3c3f44 0 45%,#d9dde0 70%,#f4f4f4)"></div><div class="label">ROLLER SHADES</div></div>

  <div class="abs closing">
    <p class="c1">Moving into your new home can be a stressful process.</p>
    <p class="c2">TALLOW PINE 58 IS ONE SOURCE FOR THE PRODUCTS YOU'LL NEED WHEN YOU MOVE IN.</p>
    <p class="c3">We can help you check several things off your to do list, so you can relax and enjoy your new home.</p>
  </div>

  <div class="abs rule"></div>
  <footer class="abs footer"><span>CALL US: (555) 014-2290</span><span>VISIT US ONLINE: WWW.TALLOWPINE58.COM</span></footer>

</main>
</body>
</html>
```